House Cleaning company in need of handout re-designs

We are looking to create a 2 sided, full color, 6" x 4" handout that promotes the company www.brisvale.com

We have one in existence that performed well, but find it too busy and would like another one designed to test performance (please see the attached files for original design). We are looking for one additional design, however depending on quality of work submitted we will select up to 5 designs.

We are looking for clean designs the will improve performance and you are 'carte blanche' on the design. That said, please ensure the following elements are present:

1) Space for an offer (i.e $39 for 3 hours of cleaning) with an expiry date.
2) Unique URL
3) Promo Code
4) Phone Number
5) The tagline of "Let Brisvale handle it" is present.
6) Logo
7) Brand colors are maintained

Also, please highlight the following:

*Eco-Friendly Cleaning Services
*Fully-Screened Cleaning Experts
*60-point checklist
*Easy Online Booking Process

Thank you.

```html
<!DOCTYPE html>
<html lang="en">
<head>
<meta charset="utf-8">
<title>Brisvale – First Clean Offer</title>
<link rel="stylesheet" href="https://fonts.googleapis.com/css2?family=Oswald:wght@500;600;700&family=Open+Sans:wght@400;600;700&family=Roboto+Condensed:ital,wght@0,400;1,700&display=swap">
<style>
  :root {
    --coral: #ee5f66;
    --teal: #5cbfae;
    --teal-deep: #1f8f85;
    --ink: #111111;
    --paper: #ffffff;
    --bar: rgba(80, 80, 80, 0.94);
    --bar-link: #8fd6cb;
  }
  html, body {
    margin: 0;
    padding: 0;
    overflow: hidden;
    background: var(--paper);
  }
  .flyer {
    position: relative;
    width: 1200px;
    height: 870px;
    overflow: hidden;
    background: var(--paper);
    font-family: "Open Sans", Arial, sans-serif;
  }
  .brand {
    position: absolute;
    left: 72px;
    top: 36px;
    margin: 0;
    font-family: "Oswald", Impact, sans-serif;
    font-weight: 600;
    font-size: 66px;
    line-height: 1;
    color: var(--coral);
    letter-spacing: 0.5px;
  }
  .tagline {
    position: absolute;
    left: 76px;
    top: 118px;
    margin: 0;
    font-size: 26px;
    line-height: 1.2;
    font-weight: 400;
    color: var(--teal);
  }
  .hero-photo {
    position: absolute;
    left: 0;
    top: 170px;
    width: 540px;
    height: 700px;
  }
  .service-points {
    position: absolute;
    left: 36px;
    top: 590px;
    width: 480px;
    margin: 0;
    padding: 0;
    list-style: none;
  }
  .service-points li {
    display: flex;
    align-items: center;
    height: 48px;
    font-size: 24px;
    font-weight: 600;
    color: var(--paper);
  }
  .service-points svg {
    width: 30px;
    height: 30px;
    margin-right: 14px;
    flex: none;
  }
  .headline {
    position: absolute;
    left: 636px;
    top: 100px;
    width: 520px;
    margin: 0;
    font-family: "Oswald", Impact, sans-serif;
    font-weight: 700;
    font-size: 64px;
    line-height: 0.98;
    letter-spacing: -1.6px;
    color: var(--ink);
  }
  .headline .accent {
    display: block;
    margin-top: 20px;
    font-family: "Open Sans", Arial, sans-serif;
    font-weight: 400;
    font-size: 40px;
    letter-spacing: 0;
    color: var(--teal);
  }
  .offer-badge {
    position: absolute;
    left: 707px;
    top: 352px;
    width: 306px;
    height: 306px;
    border-radius: 50%;
    background: var(--coral);
    color: var(--paper);
    text-align: center;
  }
  .offer-price {
    margin: 36px 0 0;
    font-family: "Oswald", Impact, sans-serif;
    font-weight: 600;
    font-size: 108px;
    line-height: 1;
  }
  .offer-price .currency {
    font-family: "Open Sans", Arial, sans-serif;
    font-weight: 400;
    font-size: 42px;
    vertical-align: 22px;
    margin-right: 8px;
  }
  .offer-title {
    margin: 10px 0 0;
    font-size: 33px;
    line-height: 1.12;
    font-weight: 400;
  }
  .offer-note {
    margin: 8px 0 0;
    font-size: 16px;
    line-height: 1.2;
    font-weight: 600;
  }
  .offer-terms {
    position: absolute;
    left: 700px;
    top: 703px;
    width: 330px;
    margin: 0;
    text-align: center;
    font-family: "Roboto Condensed", "Arial Narrow", sans-serif;
    font-size: 20px;
    line-height: 1.1;
    color: var(--ink);
  }
  .booking-bar {
    position: absolute;
    left: 0;
    bottom: 0;
    width: 100%;
    height: 66px;
    background: var(--bar);
    display: flex;
    align-items: center;
    padding-left: 206px;
    box-sizing: border-box;
    font-family: "Roboto Condensed", "Arial Narrow", sans-serif;
    font-size: 28px;
    color: var(--paper);
    white-space: nowrap;
  }
  .booking-bar .cta {
    font-weight: 700;
    font-style: italic;
    margin-right: 14px;
  }
  .booking-bar .url {
    color: var(--bar-link);
    margin-right: 14px;
  }
</style>
</head>
<body>
  <main class="flyer">
    <p class="brand">Brisvale.com</p>
    <p class="tagline">Let Brisvale handle it</p>

    <svg class="hero-photo" viewBox="0 0 540 700" preserveAspectRatio="none" role="img" aria-label="Photo of a smiling cleaner in a teal apron and yellow gloves holding a mop and a cleaning bucket">
      <defs>
        <linearGradient id="photoTone" x1="0" y1="0" x2="0" y2="1">
          <stop offset="0" stop-color="#e4f1ee"/>
          <stop offset="0.35" stop-color="#a9ddd4"/>
          <stop offset="0.65" stop-color="#4fb8aa"/>
          <stop offset="1" stop-color="#1f8f85"/>
        </linearGradient>
      </defs>
      <rect width="540" height="700" fill="url(#photoTone)"/>
    </svg>

    <ul class="service-points">
      <li><svg viewBox="0 0 30 30" aria-hidden="true"><circle cx="15" cy="15" r="14" fill="#ee5f66"/><path d="M8 15.5l4.5 4.5L22 10" fill="none" stroke="#fff" stroke-width="3" stroke-linecap="round" stroke-linejoin="round"/></svg>Eco-Friendly Cleaning Services</li>
      <li><svg viewBox="0 0 30 30" aria-hidden="true"><circle cx="15" cy="15" r="14" fill="#ee5f66"/><path d="M8 15.5l4.5 4.5L22 10" fill="none" stroke="#fff" stroke-width="3" stroke-linecap="round" stroke-linejoin="round"/></svg>Fully-Screened Cleaning Experts</li>
      <li><svg viewBox="0 0 30 30" aria-hidden="true"><circle cx="15" cy="15" r="14" fill="#ee5f66"/><path d="M8 15.5l4.5 4.5L22 10" fill="none" stroke="#fff" stroke-width="3" stroke-linecap="round" stroke-linejoin="round"/></svg>60-Point Checklist</li>
      <li><svg viewBox="0 0 30 30" aria-hidden="true"><circle cx="15" cy="15" r="14" fill="#ee5f66"/><path d="M8 15.5l4.5 4.5L22 10" fill="none" stroke="#fff" stroke-width="3" stroke-linecap="round" stroke-linejoin="round"/></svg>Easy Online Booking Process</li>
    </ul>

    <h1 class="headline">
      Do you really have<br>the time to tackle
      <span class="accent">HOUSE CHORES?</span>
    </h1>

    <section class="offer-badge">
      <p class="offer-price"><span class="currency">$</span>39</p>
      <p class="offer-title">CLEANING FOR<br>3 HOURS</p>
      <p class="offer-note">A $105 Value! Use<br>Promo Code: CA39</p>
    </section>

    <p class="offer-terms">Offer good for first time cleaning.<br>Offers expires 11/30/2014</p>

    <footer class="booking-bar">
      <span class="cta">BOOK NOW AT</span>
      <span class="url">www.brisvale.com/ca39</span>
      <span class="phone">or call 1-800-4BRISVL</span>
    </footer>
  </main>
</body>
</html>
```